Album cover design for spiritual/ceremony artist

Merel Dravin is a talented singer-songwriter who produces music for plant medicine, Breathwork, and healing ceremonies. Her musical style is a divine feminine flow of folk and indie that carries a heart healing message.

She is looking for analbum cover for her next release.

1 - We want the background to be a mandala very similar to the one I am sharing. We would like to use these same type colors and design

2 - She would like to have an image of a sufi dancer over the top of a the mandala. We ONLY WANT the silhouette of the dancer, kind of like the one shown in the brief.

3 - the text should be very simple - Just her name - “Merel Dravin” - and the title of the album which is “Low Ember”

Font styles to use
Script

Colors
EE7325
F08F49
F5BC92
FAE3D3
FDF4ED
EB3D1F
EC4F4E
F09395
F8D3D4
FCEDEE
E54698
E96AAD
F1A4CE
F9D9EA
FCEFF6
A7469A
B969AE
D3A5CF
EDDBEB
F8F0F9

Requirements
Must have
• Mandala in the background as shown in the brief, and a silhouette Sufi dancer woman over the top of it

```html
<!DOCTYPE html>
<html lang="en">
<head>
<meta charset="UTF-8">
<title>Low Ember — Merel Dravin</title>
<link href="https://fonts.googleapis.com/css2?family=Great+Vibes&family=Montserrat:wght@500&display=swap" rel="stylesheet">
<style>
  :root {
    --page-bg: #f4f2f1;
    --cover-deep: #2e0708;
    --cover-mid: #5c0d0f;
    --cover-glow: #8e1214;
    --gold-light: #fbe6a0;
    --gold: #e2b548;
    --gold-dark: #a87a1e;
    --mandala-orange: #ee7325;
    --mandala-amber: #f08f49;
    --mandala-red: #eb3d1f;
    --mandala-rose: #ec4f4e;
    --silhouette: #050303;
  }
  * { margin: 0; padding: 0; box-sizing: border-box; }
  html, body {
    width: 1200px;
    height: 868px;
    overflow: hidden;
    background: var(--page-bg);
  }
  .stage {
    position: relative;
    width: 1200px;
    height: 868px;
    display: flex;
    align-items: center;
    justify-content: center;
  }
  .album-cover {
    position: relative;
    width: 780px;
    height: 780px;
    overflow: hidden;
    background: radial-gradient(circle at 42% 48%, var(--cover-glow) 0%, var(--cover-mid) 45%, var(--cover-deep) 100%);
    box-shadow: 0 12px 30px rgba(0, 0, 0, 0.22);
  }
  .mandala {
    position: absolute;
    left: 232px;
    top: 212px;
    width: 468px;
    height: 468px;
    border-radius: 50%;
    background: radial-gradient(circle,
      var(--mandala-amber) 0%,
      var(--mandala-orange) 30%,
      var(--mandala-red) 58%,
      var(--mandala-rose) 70%,
      rgba(236, 79, 78, 0) 72%);
    opacity: 0.85;
  }
  .dancer {
    position: absolute;
    left: 368px;
    top: 330px;
    width: 330px;
    height: 390px;
  }
  .album-title {
    position: absolute;
    left: 64px;
    top: 78px;
    font-family: "Great Vibes", cursive;
    font-size: 128px;
    line-height: 1;
    font-weight: 400;
    background: linear-gradient(180deg, var(--gold-light) 0%, var(--gold) 50%, var(--gold-dark) 100%);
    -webkit-background-clip: text;
    background-clip: text;
    color: transparent;
    white-space: nowrap;
  }
  .artist-name {
    position: absolute;
    left: 352px;
    top: 214px;
    font-family: "Montserrat", sans-serif;
    font-weight: 500;
    font-size: 30px;
    letter-spacing: 1px;
    color: var(--gold);
    white-space: nowrap;
  }
</style>
</head>
<body>
  <main class="stage">
    <section class="album-cover">
      <div class="mandala" role="img" aria-label="Orange and red mandala pattern"></div>
      <svg class="dancer" viewBox="0 0 330 390" role="img" aria-label="Black silhouette of a whirling Sufi dancer">
        <defs>
          <radialGradient id="dancer-shade" cx="50%" cy="55%" r="55%">
            <stop offset="0%" stop-color="#050303" stop-opacity="0.95"/>
            <stop offset="70%" stop-color="#050303" stop-opacity="0.85"/>
            <stop offset="100%" stop-color="#050303" stop-opacity="0"/>
          </radialGradient>
        </defs>
        <ellipse cx="165" cy="215" rx="165" ry="175" fill="url(#dancer-shade)"/>
      </svg>
      <h1 class="album-title">Low Ember</h1>
      <p class="artist-name">Merel Dravin</p>
    </section>
  </main>
</body>
</html>
```